Franchise Power Point

Looking to add a strong design element to a very basic power point presentation about how to find the ideal franchise match. My website is www.brightpathventuring.com and www.vendalink/TKowalczyk

```html
<!DOCTYPE html>
<html lang="en">
<head>
<meta charset="UTF-8">
<title>How to Find the Ideal Franchise Match – Slide Deck</title>
<link href="https://fonts.googleapis.com/css2?family=Poppins:wght@400;500;600;700;800&display=swap" rel="stylesheet">
<style>
  :root {
    --navy: #1e3563;
    --navy-deep: #172b52;
    --yellow: #fdc22c;
    --ink: #111827;
    --black: #0c0c0c;
    --white: #ffffff;
    --grey: #4b5563;
    --gap: #d9d9d9;
  }
  * { box-sizing: border-box; margin: 0; padding: 0; }
  html, body { width: 1200px; height: 2365px; overflow: hidden; }
  body {
    font-family: "Poppins", sans-serif;
    background: var(--gap);
  }
  .deck {
    width: 1200px; height: 2365px;
    display: grid;
    grid-template-columns: 599px 599px;
    grid-template-rows: repeat(7, 336px);
    gap: 2px;
  }
  .slide { position: relative; overflow: hidden; background: var(--white); }
  .slide--navy { background: var(--navy); }
  .slide--black { background: var(--black); }
  .abs { position: absolute; z-index: 2; }
  .placeholder { position: absolute; z-index: 1; }

  .brand {
    position: absolute; right: 30px; bottom: 22px; z-index: 3;
    display: flex; align-items: center; gap: 6px;
    font-weight: 600; font-size: 15px; color: var(--navy);
  }
  .brand::before {
    content: ""; width: 9px; height: 9px; border-radius: 50%;
    background: var(--yellow);
  }
  .brand--light { color: var(--white); }

  .headline { font-weight: 700; line-height: 1.15; color: var(--ink); }
  .headline--light { color: var(--white); }
  .headline--navy { color: var(--navy); }
  .accent { color: var(--yellow); }

  .bullets { list-style: none; font-size: 9.5px; line-height: 16px; color: var(--grey); }
  .bullets li { position: relative; padding-left: 12px; }
  .bullets li::before {
    content: ""; position: absolute; left: 0; top: 6px;
    width: 4px; height: 4px; border-radius: 50%; background: currentColor;
  }
  .bullets--large { font-size: 12.5px; line-height: 22px; color: var(--ink); }
  .bullets--large li::before { top: 9px; }

  /* Slide 1 */
  .cover-bg { inset: 0; background: radial-gradient(circle at 70% 40%, #2b2b33 0%, #131318 55%, #08080a 100%); }
  .cover-title { left: 53px; top: 62px; font-size: 28px; }
  .presenter-photo { left: 50px; top: 225px; width: 76px; height: 76px; border-radius: 50%; background: linear-gradient(135deg, #e8c79a, #c98f5f); border: 2px solid var(--white); }
  .presenter-info { left: 143px; top: 240px; font-size: 9.5px; line-height: 13px; color: var(--white); }
  .presenter-info strong { display: block; font-weight: 700; text-decoration: underline; }
  .presenter-info span { display: block; text-decoration: underline; }
  .cover-brand { right: auto; left: 420px; bottom: 48px; font-size: 18px; }

  /* Slide 2 */
  .corner-block { left: 44px; top: 0; width: 182px; height: 62px; background: var(--yellow); }
  .hands-photo { left: 36px; top: 52px; right: 8px; height: 140px; background: linear-gradient(120deg, #7a7f6e, #b8a99a 50%, #6d6a5f); }
  .smart-title { left: 44px; top: 218px; font-size: 24px; }

  /* Slide 3 */
  .side-band { position: absolute; z-index: 0; left: 0; top: 0; width: 137px; height: 258px; background: var(--yellow); }
  .dream-title { left: 47px; top: 25px; font-size: 24px; }
  .dream-title .accent-ink { color: var(--ink); }
  .dream-photo { left: 40px; top: 160px; right: 0; height: 140px; background: linear-gradient(120deg, #6f7466, #b4a596 50%, #696459); }
  .dream-brand { bottom: 42px; }

  /* Slide 4 */
  .sand-bg { inset: 0; background: linear-gradient(160deg, #2a2a2a, #101010 60%, #050505); }
  .educated-title { left: 52px; top: 160px; font-size: 41px; line-height: 1.12; }

  /* Slide 5 */
  .pencil-icon { left: 24px; top: 52px; width: 150px; height: 145px; background: linear-gradient(135deg, #f5b942, #6fcfb9); border-radius: 10px; }
  .approach-title { left: 47px; top: 212px; font-size: 25px; }
  .step { position: absolute; z-index: 2; display: flex; align-items: center; gap: 14px; padding: 0 14px; border-radius: 4px; font-size: 9px; line-height: 11px; color: var(--ink); white-space: nowrap; }
  .step b { font-size: 30px; font-weight: 700; color: var(--navy); }
  .step--white { background: var(--white); box-shadow: 0 3px 10px rgba(0,0,0,.15); }
  .step--navy { background: var(--navy); color: var(--white); }
  .step--navy b { color: var(--white); }
  .step--yellow { background: var(--yellow); }
  .step-1 { left: 251px; top: 45px; width: 197px; height: 43px; }
  .step-2 { left: 303px; top: 107px; width: 203px; height: 44px; }
  .step-3 { left: 220px; top: 167px; width: 204px; height: 43px; font-size: 8.5px; line-height: 10px; }
  .step-4 { left: 267px; top: 226px; width: 204px; height: 46px; }

  /* Slide 6 */
  .questions-title { left: 44px; top: 30px; font-size: 25px; }
  .chat-icon { left: 435px; top: 22px; width: 92px; height: 92px; background: linear-gradient(135deg, #7fd6c6, #f5b942); border-radius: 10px; }
  .questions-col-1 { left: 44px; top: 180px; }
  .questions-col-2 { left: 335px; top: 180px; }

  /* Slide 7 */
  .research-icon { left: 47px; top: 30px; width: 118px; height: 107px; background: linear-gradient(135deg, #8fb8e8, #e76f7a); border-radius: 10px; }
  .research-title { left: 192px; top: 44px; font-size: 25px; }
  .research-col-1 { left: 196px; top: 160px; }
  .research-col-2 { left: 405px; top: 160px; }

  /* Slide 8 */
  .brain-icon { left: 36px; top: 40px; width: 197px; height: 196px; background: radial-gradient(circle, #fdc22c 0%, #e0a51e 55%, transparent 72%); }
  .decision-title { left: 283px; top: 118px; font-size: 28px; }
  .decision-sub { left: 283px; top: 156px; font-size: 16px; color: var(--white); }

  /* Slide 9 */
  .twin-brain { left: 30px; top: 30px; width: 213px; height: 222px; background: radial-gradient(circle, #5fc3a9 0%, #b9bcc1 55%, transparent 72%); }
  .spirit-title { left: 290px; top: 60px; font-size: 24px; }
  .spirit-sub { left: 290px; top: 128px; font-size: 17px; line-height: 21px; color: var(--ink); }

  /* Slide 10 */
  .dam-text { left: 0; right: 0; top: 92px; text-align: center; font-size: 23px; line-height: 1.2; color: var(--white); }
  .dam-text b { font-weight: 700; }

  /* Slide 11 */
  .book-cover { left: 58px; top: 43px; width: 197px; height: 240px; background: linear-gradient(180deg, #2f9a8c, #1f5f7a); }
  .booth-text { left: 303px; top: 160px; font-size: 15px; line-height: 20px; color: var(--white); }
  .booth-text b { font-weight: 700; }

  /* Slide 12 & 13 */
  .thumb-icon { width: 140px; height: 135px; background: radial-gradient(circle at 50% 65%, #f8c9a0 0%, #7fb2e6 45%, transparent 70%); }
  .thumb-a { left: 36px; top: 48px; }
  .thumb-b { left: 264px; top: 30px; }
  .dozen-title { font-size: 36px; line-height: 1.12; }
  .dozen-a { left: 227px; top: 50px; }
  .dozen-b { left: 55px; top: 45px; }
  .dozen-a-col-1 { left: 227px; top: 198px; }
  .dozen-a-col-2 { left: 376px; top: 198px; }
  .dozen-b-col-1 { left: 55px; top: 200px; }
  .dozen-b-col-2 { left: 239px; top: 200px; }

  /* Slide 14 */
  .closing-brand { left: 0; right: 0; top: 64px; display: flex; flex-direction: column; align-items: center; color: var(--white); }
  .closing-brand .name { display: flex; align-items: center; gap: 8px; font-size: 28px; font-weight: 600; }
  .closing-brand .name::before { content: ""; width: 12px; height: 12px; border-radius: 50%; background: var(--yellow); }
  .closing-brand .tagline { font-size: 9px; margin-top: 2px; }
  .thanks { left: 0; right: 0; top: 196px; text-align: center; font-size: 46px; font-weight: 700; color: var(--white); }
</style>
</head>
<body>
<main class="deck">

  <!-- Cover -->
  <section class="slide">
    <div class="placeholder cover-bg" role="img" aria-label="Night sky with circular star trails"></div>
    <h1 class="abs headline headline--light cover-title">How to<br>Find <span class="accent">the Ideal<br>Franchise</span><br>Match</h1>
    <div class="placeholder presenter-photo" role="img" aria-label="Portrait photo of the presenter"></div>
    <div class="abs presenter-info">
      <strong>Tessa Kowalczyk</strong>
      443.555.0142
      <span>tkowalczyk@vendalink.com</span>
      <span>http://www.brightpathventuring.com</span>
    </div>
    <div class="brand brand--light cover-brand">Vendalink</div>
  </section>

  <!-- Smart decisions -->
  <section class="slide">
    <div class="abs corner-block"></div>
    <div class="placeholder hands-photo" role="img" aria-label="Photo of two people holding hands"></div>
    <h2 class="abs headline smart-title">Smart Franchise<br>Decisions Using Logic<br>and Intuition</h2>
    <div class="brand">Vendalink</div>
  </section>

  <!-- Dream vs nightmare -->
  <section class="slide">
    <div class="side-band"></div>
    <h2 class="abs headline dream-title"><span class="accent-ink">Do not</span> let your<br>Entrepreneurial Dream turn<br>a Technicians Nightmare</h2>
    <div class="placeholder dream-photo" role="img" aria-label="Photo of two people holding hands"></div>
    <div class="brand brand--light dream-brand">Vendalink</div>
  </section>

  <!-- Educated approach -->
  <section class="slide slide--black">
    <div class="placeholder sand-bg" role="img" aria-label="Dark rippled sand texture"></div>
    <h2 class="abs headline headline--light educated-title">Use <span class="accent">the<br>Educated</span><br>Approach</h2>
    <div class="brand brand--light">Vendalink</div>
  </section>

  <!-- What is the approach -->
  <section class="slide">
    <div class="placeholder pencil-icon" role="img" aria-label="Illustration of a hand holding a pencil"></div>
    <h2 class="abs headline headline--navy approach-title">What is the<br>Educated<br>Approach?</h2>
    <div class="step step--white step-1"><b>1</b><span>Find Define<br>the ideal Fit</span></div>
    <div class="step step--navy step-2"><b>2</b><span>Focus on options that<br>fit your strengths</span></div>
    <div class="step step--white step-3"><b>3</b><span>Focus on options that will meet<br>your lifestyle and financial goals<br>while reducing risk</span></div>
    <div class="step step--yellow step-4"><b>4</b><span>Put yourself at the<br>center of the search</span></div>
    <div class="brand">Vendalink</div>
  </section>

  <!-- Key questions -->
  <section class="slide">
    <h2 class="abs headline headline--navy questions-title">Sample Key<br>Questions for the<br>Educated Approach</h2>
    <div class="placeholder chat-icon" role="img" aria-label="Illustration of chat speech bubbles"></div>
    <ul class="abs bullets questions-col-1">
      <li>Proper investment level</li>
      <li>Skill set and background / personality matching</li>
      <li>Return goals – short, mid and long term</li>
      <li>Employee profile: numbers &amp; backgrounds</li>
      <li>Sales, marketing and advertising</li>
      <li>Concerns around the economy</li>
    </ul>
    <ul class="abs bullets questions-col-2">
      <li>Need vs want</li>
      <li>Residual / Repeat / Reoccurring</li>
      <li>Status</li>
      <li>B2B vs B2C</li>
      <li>Full time vs part time vs. managed services</li>
    </ul>
    <div class="brand">Vendalink</div>
  </section>

  <!-- Research method -->
  <section class="slide">
    <div class="placeholder research-icon" role="img" aria-label="Illustration of a screen with a magnifying glass"></div>
    <h2 class="abs headline research-title">The<br>Research<br>Method</h2>
    <ul class="abs bullets research-col-1">
      <li>Define your ideal match</li>
      <li>Establish contact with target franchisor</li>
      <li>Work through their standard process</li>
      <li>Review FDD</li>
      <li>Validate with franchisees</li>
    </ul>
    <ul class="abs bullets research-col-2">
      <li>Explore financing options</li>
      <li>Discuss territory</li>
      <li>Put together cash flow projections</li>
      <li>Attend Discovery Day</li>
      <li>Make a decision</li>
    </ul>
    <div class="brand">Vendalink</div>
  </section>

  <!-- Decision making -->
  <section class="slide slide--navy">
    <div class="placeholder brain-icon" role="img" aria-label="Illustration of a yellow brain with sparkles"></div>
    <h2 class="abs headline headline--light decision-title">Decision Making</h2>
    <p class="abs decision-sub">Right Brain vs. Left Brain</p>
    <div class="brand brand--light">Vendalink</div>
  </section>

  <!-- Human spirit -->
  <section class="slide">
    <div class="placeholder twin-brain" role="img" aria-label="Illustration of a two-tone brain with sparkles"></div>
    <h2 class="abs headline spirit-title">The human spirit<br>resist’s change</h2>
    <p class="abs spirit-sub">The human spirit<br>resist’s change</p>
    <div class="brand">Vendalink</div>
  </section>

  <!-- Dam or river -->
  <section class="slide slide--black">
    <p class="abs dam-text">Are you <b>the</b><br><b>dam or</b> are you<br><b>the River?</b></p>
    <div class="brand brand--light">Vendalink</div>
  </section>

  <!-- Booth offer -->
  <section class="slide slide--navy">
    <div class="placeholder book-cover" role="img" aria-label="Cover of a franchise buying guidebook with an apple illustration"></div>
    <p class="abs booth-text">Stop by <b>my Booth,</b> Ask Me<br><b>ANY Question</b> and<br>Receive a <b>Free Copy</b> of<br>The <b>Franchisee Fieldbook</b></p>
    <div class="brand brand--light">Vendalink</div>
  </section>

  <!-- Top dozen part 1 -->
  <section class="slide">
    <div class="placeholder thumb-icon thumb-a" role="img" aria-label="Illustration of a thumbs-up hand with stars"></div>
    <h2 class="abs headline headline--navy dozen-title dozen-a">My Top<br>Dozen for<br>2024</h2>
    <ul class="abs bullets bullets--large dozen-a-col-1">
      <li>Pet Options</li>
      <li>Real Estate Options</li>
      <li>Mental Health</li>
    </ul>
    <ul class="abs bullets bullets--large dozen-a-col-2">
      <li>Pet Options</li>
      <li>Real Estate Options</li>
      <li>Mental Health</li>
    </ul>
    <div class="brand">Vendalink</div>
  </section>

  <!-- Top dozen part 2 -->
  <section class="slide">
    <h2 class="abs headline headline--navy dozen-title dozen-b">My Top<br>Dozen for<br><span class="accent">2024</span></h2>
    <div class="placeholder thumb-icon thumb-b" role="img" aria-label="Illustration of a thumbs-up hand with stars"></div>
    <ul class="abs bullets bullets--large dozen-b-col-1">
      <li>Emergency Restoration</li>
      <li>Low Status Options</li>
      <li>Home Services</li>
    </ul>
    <ul class="abs bullets bullets--large dozen-b-col-2">
      <li>Rental Options</li>
      <li>Clothing Recyling</li>
      <li>Food Trucks/Restaurants</li>
    </ul>
    <div class="brand">Vendalink</div>
  </section>

  <!-- Closing -->
  <section class="slide slide--navy">
    <div class="abs closing-brand">
      <span class="name">Vendalink</span>
      <span class="tagline">Helping People Build Their Futures</span>
    </div>
    <p class="abs thanks">THANK YOU</p>
  </section>

</main>
</body>
</html>
```